Varnel Supply requires a new business card.

We are an online professional tool store.

Target Market(s)

We target the professional technician.

Industry/Entity Type

Business

Contact Information for Business Card

VarnelSupply.com.au

sales@varnelsupply.example

Requirements
Must have
• Needs to look commercial and professional
Should not have
• No Australian Colors, maps or shapes.
• No Shapes of Tools

```html
<!DOCTYPE html>
<html lang="en">
<head>
<meta charset="utf-8">
<title>Varnel Supply – Business Card</title>
<link href="https://fonts.googleapis.com/css2?family=Work+Sans:wght@400;500;600&display=swap" rel="stylesheet">
<style>
  :root {
    --backdrop: #161616;
    --card: #232323;
    --card-edge: #2c2c2c;
    --brand-blue: #3a4fc0;
    --accent-cyan: #1e9fd8;
    --text-light: #f1f1f1;
    --text-muted: #b9b9b9;
  }
  * { margin: 0; padding: 0; box-sizing: border-box; }
  html, body {
    width: 1200px; height: 900px; overflow: hidden;
    background: var(--backdrop);
    font-family: "Work Sans", Arial, sans-serif;
  }
  .stage {
    width: 1200px; height: 900px;
    display: flex; flex-direction: column; align-items: center; justify-content: center;
    gap: 36px;
  }
  .card {
    width: 700px; height: 400px;
    background: var(--card);
    border: 1px solid var(--card-edge);
    position: relative;
    box-shadow: 0 10px 30px rgba(0,0,0,0.5);
  }
  /* Front */
  .card-front { display: flex; flex-direction: column; align-items: center; justify-content: center; }
  .brand-mark { display: flex; align-items: center; gap: 14px; }
  .brand-dot { width: 22px; height: 22px; border-radius: 50%; }
  .brand-name { font-weight: 600; letter-spacing: 0.5px; }
  .card-front .brand-dot { background: var(--text-muted); }
  .card-front .brand-name { color: var(--text-muted); font-size: 50px; }
  .front-web {
    position: absolute; bottom: 58px; left: 0; right: 0; text-align: center;
    font-size: 19px; color: var(--text-light); letter-spacing: 0.8px;
  }
  .front-web .web-highlight { color: var(--accent-cyan); }
  /* Back */
  .card-back { display: flex; align-items: center; padding: 0 60px 0 50px; }
  .card-back .brand-mark { width: 300px; }
  .card-back .brand-dot { background: var(--brand-blue); }
  .card-back .brand-name { color: var(--brand-blue); font-size: 38px; }
  .divider { width: 2px; height: 230px; background: var(--accent-cyan); margin: 0 40px 0 20px; }
  .contact { color: var(--text-light); }
  .person-name { color: var(--accent-cyan); font-size: 30px; font-weight: 500; letter-spacing: 1px; }
  .person-role { font-size: 18px; letter-spacing: 0.8px; margin-bottom: 18px; }
  .address { font-size: 19px; line-height: 1.35; letter-spacing: 0.8px; margin-bottom: 14px; }
  .contact-list { list-style: none; }
  .contact-list li { display: flex; align-items: center; gap: 14px; font-size: 19px; letter-spacing: 0.8px; line-height: 1.45; }
  .contact-list svg { width: 17px; height: 17px; flex: none; fill: var(--accent-cyan); }
</style>
</head>
<body>
<main class="stage">
  <section class="card card-front">
    <div class="brand-mark">
      <span class="brand-dot"></span>
      <span class="brand-name">Varnel Supply</span>
    </div>
    <p class="front-web">www.<span class="web-highlight">VarnelSupply</span>.com.au</p>
  </section>

  <section class="card card-back">
    <div class="brand-mark">
      <span class="brand-dot"></span>
      <span class="brand-name">Varnel Supply</span>
    </div>
    <div class="divider"></div>
    <div class="contact">
      <h1 class="person-name">DANIEL ROWE</h1>
      <p class="person-role">FOUNDER</p>
      <p class="address">14 Harlow Court,<br>Easton TX 77500</p>
      <ul class="contact-list">
        <li>
          <svg viewBox="0 0 24 24" aria-hidden="true"><path d="M6.6 10.8a15 15 0 0 0 6.6 6.6l2.2-2.2c.3-.3.7-.4 1-.2 1.1.4 2.3.6 3.6.6.6 0 1 .4 1 1V20c0 .6-.4 1-1 1A17 17 0 0 1 3 4c0-.6.4-1 1-1h3.5c.6 0 1 .4 1 1 0 1.3.2 2.5.6 3.6.1.3 0 .7-.2 1z"/></svg>
          (123) 456-7890
        </li>
        <li>
          <svg viewBox="0 0 24 24" aria-hidden="true"><path d="M7 1h10a2 2 0 0 1 2 2v18a2 2 0 0 1-2 2H7a2 2 0 0 1-2-2V3a2 2 0 0 1 2-2zm0 3v14h10V4zm5 15.5a1 1 0 1 0 0 2 1 1 0 0 0 0-2z"/></svg>
          (123) 456-7890
        </li>
        <li>
          <svg viewBox="0 0 24 24" aria-hidden="true"><path d="M2 5h20v14H2zm2 2v.5l8 5 8-5V7zm0 2.8V17h16V9.8l-8 5z"/></svg>
          sales@varnelsupply.example
        </li>
        <li>
          <svg viewBox="0 0 24 24" aria-hidden="true"><path d="M12 2a10 10 0 1 0 0 20 10 10 0 0 0 0-20zm6.9 9h-3a15 15 0 0 0-1.2-5.7A8 8 0 0 1 18.9 11zM12 4c.9 1.2 1.8 3.6 1.9 7h-3.8c.1-3.4 1-5.8 1.9-7zM9.3 5.3A15 15 0 0 0 8.1 11h-3a8 8 0 0 1 4.2-5.7zM5.1 13h3a15 15 0 0 0 1.2 5.7A8 8 0 0 1 5.1 13zM12 20c-.9-1.2-1.8-3.6-1.9-7h3.8c-.1 3.4-1 5.8-1.9 7zm2.7-1.3a15 15 0 0 0 1.2-5.7h3a8 8 0 0 1-4.2 5.7z"/></svg>
          VarnelSupply.com.au
        </li>
      </ul>
    </div>
  </section>
</main>
</body>
</html>
```